Australian Trucking Company Requires Professional Looking Stationary

We require a professional looking stationary design that incorporates our newly designed logo.

Our business, called "Marlow Haul Contracting", provides contracting work, transport and logistics to business in Western Australia particularly with links to the mining sector.

We are a small business looking to expand and our new logo and our new stationary will help develop our brand image in our market place.

Target Market(s)

Businesses and Corporation with links to the Mining Sector

Industry/Entity Type

Small Business

Requirements
Must have
• The letterhead must have the following details:
The new logo

Text saying: "Marlow Holdings Pty Ltd (ACN 352 018 927) ATF The Marlow Discretionary Trust T/AS"
"ABN 72 483 910 615"
Address "P.O Box 817 Wexbridge WA, 6999"
Phone: 08 9555 0182
Email: marlowhaul@inboxmail.example

The text on the letterhead should be editable as the details are likely to change in the near future. Provision should be made for a website address all though one isn't available at the moment.

The styling, layout and font text is entirely up to the designer.

```html
<!DOCTYPE html>
<html lang="en">
<head>
<meta charset="utf-8">
<title>Marlow Haul Contracting – Stationery</title>
<link rel="stylesheet" href="https://fonts.googleapis.com/css2?family=Source+Sans+3:wght@400;600;700&display=swap">
<style>
  :root {
    --brand-red: #e30613;
    --brand-red-dark: #b8000d;
    --ink: #1a1a1a;
    --paper: #ffffff;
    --backdrop: #d9d9d9;
    --shade: rgba(0,0,0,0.14);
    --faint: rgba(255,255,255,0.16);
  }
  * { box-sizing: border-box; margin: 0; padding: 0; }
  html, body { width: 848px; height: 1200px; overflow: hidden; }
  body {
    background: var(--backdrop);
    font-family: "Source Sans 3", "Myriad Pro", Arial, sans-serif;
    color: var(--ink);
    position: relative;
  }

  /* Business card – reverse */
  .card-back {
    position: absolute; left: 305px; top: 43px;
    width: 261px; height: 153px;
    background: var(--brand-red);
    overflow: hidden;
  }
  .card-back .truck-art {
    position: absolute; left: 0; top: 70px;
    width: 80px; height: 83px;
    background: linear-gradient(135deg, var(--faint), rgba(255,255,255,0.06));
  }

  /* Business card – front */
  .card-front {
    position: absolute; left: 494px; top: 87px;
    width: 260px; height: 153px;
    background: var(--paper);
    box-shadow: 8px 8px 0 var(--shade);
    padding: 22px 10px 0 12px;
  }
  .wordmark {
    display: flex; align-items: center; gap: 6px;
    font-weight: 700; color: var(--brand-red);
    text-transform: uppercase; line-height: 0.95;
  }
  .wordmark .mark-square { background: #7a7a7a; flex: none; }
  .card-front .wordmark { font-size: 9px; }
  .card-front .wordmark .mark-square { width: 24px; height: 24px; }

  .details { display: grid; grid-template-columns: auto auto; justify-content: space-between; }
  .details p { line-height: 1.35; white-space: nowrap; }
  .details strong { font-weight: 700; }
  .card-front .details { margin-top: 14px; font-size: 5.6px; column-gap: 6px; }

  /* Envelope – opened, flat */
  .envelope-back {
    position: absolute; left: 126px; top: 330px;
    width: 665px; height: 400px;
  }

  /* Envelope – front */
  .envelope-front {
    position: absolute; left: 126px; top: 770px;
    width: 665px; height: 305px;
    background: var(--paper);
    box-shadow: 8px 8px 0 var(--shade);
    border: 1px solid #cfcfcf;
  }
  .envelope-front .footer {
    position: absolute; left: 70px; right: 36px; top: 236px;
    display: flex; align-items: center;
  }
  .envelope-front .wordmark { font-size: 11px; width: 178px; flex: none; }
  .envelope-front .wordmark .mark-square { width: 34px; height: 34px; }
  .envelope-front .details {
    font-size: 8.5px; flex: 1;
    grid-template-columns: auto auto; justify-content: start; column-gap: 24px;
  }
</style>
</head>
<body>

  <section class="card-back" aria-label="Business card reverse">
    <div class="truck-art" role="img" aria-label="Faint truck illustration"></div>
  </section>

  <section class="card-front" aria-label="Business card front">
    <div class="wordmark"><span class="mark-square"></span><span>Marlow Haul<br>Contracting</span></div>
    <div class="details">
      <div class="col-contact">
        <p><strong>Marlow Holdings Pty Ltd</strong></p>
        <p>P.O Box 817 Wexbridge WA, 6999</p>
        <p><strong>T :</strong> 08 9555 0182 &nbsp;<strong>E :</strong> marlowhaul@inboxmail.example</p>
      </div>
      <div class="col-legal">
        <p><strong>ABN</strong> 72 483 910 615</p>
        <p><strong>ACN</strong> 352 018 927</p>
        <p><strong>ATF</strong> The Marlow Discretionary Trust T/AS</p>
      </div>
    </div>
  </section>

  <svg class="envelope-back" viewBox="0 0 665 400" aria-label="Envelope reverse, opened flat">
    <defs>
      <linearGradient id="liner" x1="0" y1="0" x2="1" y2="1">
        <stop offset="0.45" stop-color="#e30613"/>
        <stop offset="1" stop-color="#b8000d"/>
      </linearGradient>
      <linearGradient id="truckFade" x1="0" y1="0" x2="1" y2="1">
        <stop offset="0" stop-color="#fff" stop-opacity="0.2"/>
        <stop offset="1" stop-color="#fff" stop-opacity="0.05"/>
      </linearGradient>
    </defs>
    <rect x="0" y="160" width="665" height="240" fill="#ffffff" stroke="#cfcfcf"/>
    <path d="M0 160 L332 0 L665 160 Z" fill="url(#liner)"/>
    <path d="M90 160 L180 70 L300 70 L300 160 Z" fill="url(#truckFade)" role="img" aria-label="Faint truck illustration"/>
    <path d="M0 160 L332 330 L665 160" fill="none" stroke="#cfcfcf"/>
    <path d="M0 400 L260 250 M665 400 L405 250" fill="none" stroke="#e0e0e0"/>
  </svg>

  <section class="envelope-front" aria-label="DL envelope front">
    <div class="footer">
      <div class="wordmark"><span class="mark-square"></span><span>Marlow Haul<br>Contracting</span></div>
      <div class="details">
        <div class="col-contact">
          <p><strong>Marlow Holdings Pty Ltd</strong></p>
          <p>P.O Box 817 Wexbridge WA, 6999</p>
          <p><strong>T :</strong> 08 9555 0182 &nbsp;<strong>E :</strong> marlowhaul@inboxmail.example</p>
        </div>
        <div class="col-legal">
          <p><strong>ABN</strong> 72 483 910 615</p>
          <p><strong>ACN</strong> 352 018 927</p>
          <p><strong>ATF</strong> The Marlow Discretionary Trust T/AS</p>
        </div>
      </div>
    </div>
  </section>

</body>
</html>
```